Wempixa socks

I’m starting a sock company that only sells solid color socks made out of bamboo . Bamboo is a
Performance textile that wicks moisture , and incredible softness it’s the best textile for sock
Manufacturing in my opinion . So wrap your mind
Around this the socks are going to be packaged in
A box that looks like a 8 pack of crayons see pic’s
Difference is it’s going to be 6 pairs of socks in the box and there going to be in whatever the hottest
Color’s are for the season. winter crews ,spring 1/4
Crews mixed with ankle socks , Summer no looks
With ankle , and fall mixed with crew 1/4 crew and ankle remember no print solid colors only the packaging and and logo are more important then the product it’s going to be sold at gift boutiques
Around America

```html
<!DOCTYPE html>
<html lang="en">
<head>
<meta charset="utf-8">
<title>Wempixa's Bamboo Performance Socks – Box Front</title>
<link href="https://fonts.googleapis.com/css2?family=Lilita+One&family=Montserrat:wght@600;800&display=swap" rel="stylesheet">
<style>
  :root {
    --page-bg: #e8e8e8;
    --yellow-light: #fbe24e;
    --yellow: #f4cd16;
    --yellow-edge: #e9b80c;
    --brown: #5a2a10;
    --red: #d62828;
    --red-dark: #9e1620;
    --white: #ffffff;
    --green-light: #9bcf4f;
    --green: #4f9a2a;
    --ink: #3a2a10;
  }
  html, body {
    margin: 0;
    padding: 0;
    width: 1200px;
    height: 840px;
    overflow: hidden;
    background: var(--page-bg);
  }
  .canvas {
    position: relative;
    width: 1200px;
    height: 840px;
    overflow: hidden;
  }
  .box-front {
    position: absolute;
    left: 320px;
    top: 40px;
    width: 560px;
    height: 760px;
  }
  .box-front svg { display: block; width: 100%; height: 100%; }
  .brand-title {
    font-family: "Lilita One", "Arial Black", sans-serif;
    font-size: 76px;
    fill: var(--brown);
    letter-spacing: 2px;
  }
  .ribbon-text {
    font-family: "Montserrat", Arial, sans-serif;
    font-weight: 800;
    font-size: 23px;
    fill: var(--white);
    letter-spacing: 1px;
  }
  .badge-word {
    font-family: "Montserrat", Arial, sans-serif;
    font-weight: 800;
    font-size: 30px;
    fill: var(--white);
  }
  .badge-number {
    font-family: "Lilita One", "Arial Black", sans-serif;
    font-size: 118px;
    fill: var(--white);
  }
  .feature-label {
    font-family: "Montserrat", Arial, sans-serif;
    font-weight: 600;
    font-size: 9px;
    fill: var(--ink);
    letter-spacing: 0.3px;
  }
  .site-url {
    font-family: "Montserrat", Arial, sans-serif;
    font-weight: 800;
    font-size: 12px;
    fill: var(--ink);
    letter-spacing: 1.5px;
  }
  .feature-icon {
    fill: none;
    stroke: var(--ink);
    stroke-width: 1.8;
    stroke-linecap: round;
    stroke-linejoin: round;
  }
</style>
</head>
<body>
<main class="canvas">
  <section class="box-front">
    <svg viewBox="0 0 560 760" xmlns="http://www.w3.org/2000/svg">
      <defs>
        <radialGradient id="panel-fill" cx="50%" cy="40%" r="75%">
          <stop offset="0%" stop-color="var(--yellow-light)"/>
          <stop offset="70%" stop-color="var(--yellow)"/>
          <stop offset="100%" stop-color="var(--yellow-edge)"/>
        </radialGradient>
        <linearGradient id="sock-tones" x1="0" y1="0" x2="1" y2="0">
          <stop offset="0%" stop-color="#b8263a"/>
          <stop offset="20%" stop-color="#8fb8e6"/>
          <stop offset="40%" stop-color="#e44a4a"/>
          <stop offset="58%" stop-color="#ece0e6"/>
          <stop offset="78%" stop-color="#f59a5e"/>
          <stop offset="100%" stop-color="#a48bd0"/>
        </linearGradient>
        <linearGradient id="bamboo-tones" x1="0" y1="0" x2="1" y2="0">
          <stop offset="0%" stop-color="var(--green)"/>
          <stop offset="100%" stop-color="var(--green-light)"/>
        </linearGradient>
        <path id="ribbon-arc" d="M120 433 Q280 412 440 433"/>
      </defs>

      <rect class="panel" width="560" height="760" fill="url(#panel-fill)"/>

      <g class="bamboo-left" role="img" aria-label="Bamboo stalks and leaves along the left edge">
        <rect x="0" y="0" width="28" height="150" fill="url(#bamboo-tones)" opacity="0.85"/>
        <rect x="0" y="440" width="62" height="320" fill="url(#bamboo-tones)"/>
      </g>
      <g class="bamboo-right" role="img" aria-label="Bamboo stalks and leaves along the right edge">
        <rect x="498" y="340" width="62" height="420" fill="url(#bamboo-tones)"/>
      </g>

      <text class="brand-title" x="280" y="128" text-anchor="middle">WEMPIXA'S</text>

      <path class="sock-window" role="img" aria-label="Six rolled solid colour socks seen through the box window"
            d="M62 178 Q280 198 498 178 L498 252 Q280 372 62 252 Z"
            fill="url(#sock-tones)" stroke="var(--yellow-edge)" stroke-width="3"/>

      <g class="ribbon">
        <path d="M78 420 L124 414 L124 466 L78 472 L96 446 Z" fill="var(--red-dark)"/>
        <path d="M482 420 L436 414 L436 466 L482 472 L464 446 Z" fill="var(--red-dark)"/>
        <path d="M110 408 Q280 386 450 408 L450 456 Q280 434 110 456 Z" fill="var(--red)"/>
        <text class="ribbon-text" text-anchor="middle"><textPath href="#ribbon-arc" startOffset="50%">BAMBOO PERFORMANCE</textPath></text>
      </g>

      <g class="count-badge">
        <circle cx="280" cy="560" r="100" fill="var(--red)"/>
        <text class="badge-word" x="280" y="512" text-anchor="middle">SOCK'S</text>
        <text class="badge-number" x="280" y="612" text-anchor="middle">6</text>
        <text class="badge-word" x="280" y="646" text-anchor="middle">PAIR</text>
      </g>

      <g class="features">
        <g class="feature-soft">
          <path class="feature-icon" d="M170 704 L190 678 M174 700 Q178 680 192 676 Q190 692 176 700"/>
          <text class="feature-label" x="180" y="722" text-anchor="middle">SUPER SOFT</text>
        </g>
        <g class="feature-wicking">
          <path class="feature-icon" d="M268 680 v10 M280 680 v10 M292 680 v10 M266 698 h28 M266 704 h28"/>
          <text class="feature-label" x="280" y="722" text-anchor="middle">MOISTURE WICKING</text>
        </g>
        <g class="feature-pure">
          <circle class="feature-icon" cx="380" cy="690" r="12"/>
          <path class="feature-icon" d="M374 690 l4 4 l8 -8"/>
          <text class="feature-label" x="380" y="722" text-anchor="middle">PURE BAMBOO</text>
        </g>
      </g>

      <text class="site-url" x="280" y="748" text-anchor="middle">www.wempixa.com</text>
    </svg>
  </section>
</main>
</body>
</html>
```